Esthetically Pleasing Core Values and Brand Promise for Accounting Firm

I would like a cohesive design that ties together my core values and brand promise. My firm, Maple Finch Advisory, provides accounting work to small businesses. I prefer modern and clean designs. I want my Core Values and Brand Promise to represent me - sole entrepreneur, married, mother of two kids, modern esthetics, clean lines, organized, colorful (teals, greys, white, yellows)

Industry/Entity Type

Public Accounting

Colors
33b8a4

```html
<!DOCTYPE html>
<html lang="en">
<head>
<meta charset="utf-8">
<title>Core Values – Maple Finch Advisory</title>
<link href="https://fonts.googleapis.com/css2?family=Poppins:wght@400;500;700;800&display=swap" rel="stylesheet">
<style>
  :root {
    --teal: #46adad;
    --charcoal: #4a4a4a;
    --ink: #555555;
    --yellow: #fcee6d;
    --paper: #ffffff;
    --backdrop: #bdbdbd;
  }
  * { margin: 0; padding: 0; box-sizing: border-box; }
  html, body { width: 1200px; height: 2363px; overflow: hidden; }
  body { background: var(--backdrop); font-family: 'Poppins', sans-serif; position: relative; }

  .poster {
    position: absolute; left: 60px; top: 418px;
    width: 1080px; height: 1527px;
    background: var(--paper);
    box-shadow: 0 14px 40px rgba(0,0,0,0.35);
  }
  .poster__topbar { position: absolute; left: 0; top: 0; width: 100%; height: 16px; background: var(--yellow); }

  .title { position: absolute; left: 0; width: 100%; text-align: center; font-weight: 800; line-height: 1; letter-spacing: -2px; }
  .title--core { top: 42px; font-size: 136px; color: var(--teal); }
  .title--values { top: 154px; font-size: 142px; color: var(--charcoal); }

  .icon { position: absolute; width: 88px; height: 88px; }
  .icon circle.ring { fill: #fff; stroke: var(--yellow); stroke-width: 3.5; }
  .icon .glyph { fill: none; stroke: #333; stroke-width: 2; stroke-linecap: round; stroke-linejoin: round; }

  .value { position: absolute; width: 420px; }
  .value--left { right: 563px; text-align: right; }
  .value--right { left: 566px; text-align: left; }
  .value__name { font-size: 35px; font-weight: 800; color: var(--teal); line-height: 1; margin-bottom: 14px; }
  .value__text { font-size: 23px; font-weight: 400; color: var(--ink); line-height: 33px; }

  .promise { position: absolute; left: 0; top: 1000px; width: 100%; text-align: center; }
  .promise__name { font-size: 36px; font-weight: 800; color: var(--teal); line-height: 1.1; }
  .promise__text { font-size: 23px; color: var(--ink); margin-top: 4px; }

  .services { position: absolute; left: 0; top: 1091px; width: 100%; height: 285px; background: var(--teal); }
  .service { position: absolute; top: 26px; width: 420px; color: #fff; }
  .service--left { right: 563px; text-align: right; }
  .service--right { left: 566px; }
  .service__name { font-size: 37px; font-weight: 800; line-height: 1; margin-bottom: 14px; }
  .service__text { font-size: 22.5px; font-weight: 500; line-height: 33px; }

  .site { position: absolute; left: 0; top: 1420px; width: 100%; text-align: center; font-size: 38px; line-height: 1.2; color: var(--ink); }
  .site__name { color: var(--teal); font-weight: 700; }
</style>
</head>
<body>
<main class="poster">
  <div class="poster__topbar"></div>

  <h1 class="title title--core">CORE</h1>
  <h1 class="title title--values">VALUES</h1>

  <!-- row one icons -->
  <svg class="icon" style="left:424px; top:341px" viewBox="0 0 88 88" aria-hidden="true">
    <circle class="ring" cx="44" cy="44" r="41"/>
    <g class="glyph">
      <rect x="33" y="40" width="22" height="20" rx="5"/>
      <path d="M38 40v8M44 40v8M50 40v8M36 60v6h16v-6"/>
      <path d="M44 22v10M34 26l4 8M54 26l-4 8M27 33l7 5M61 33l-7 5"/>
    </g>
  </svg>
  <svg class="icon" style="left:566px; top:341px" viewBox="0 0 88 88" aria-hidden="true">
    <circle class="ring" cx="44" cy="44" r="41"/>
    <g class="glyph">
      <path d="M22 48l14-14 8 4 8-6 14 14-16 16z"/>
      <path d="M36 48l8 8M42 44l8 8M48 40l6 6"/>
    </g>
  </svg>

  <section class="value value--left" style="top:455px">
    <h2 class="value__name">EMPOWER</h2>
    <p class="value__text">We are dedicated, appreciative<br>and respectful of people's time<br>and purpose.</p>
  </section>
  <section class="value value--right" style="top:455px">
    <h2 class="value__name">RECTITUDE</h2>
    <p class="value__text">We know the difference between<br>what we have the right to do and<br>what the right thing to do is.</p>
  </section>

  <!-- row two icons -->
  <svg class="icon" style="left:424px; top:637px" viewBox="0 0 88 88" aria-hidden="true">
    <circle class="ring" cx="44" cy="44" r="41"/>
    <g class="glyph">
      <path d="M44 26l5 11 12 1-9 8 3 12-11-6-11 6 3-12-9-8 12-1z"/>
    </g>
  </svg>
  <svg class="icon" style="left:566px; top:637px" viewBox="0 0 88 88" aria-hidden="true">
    <circle class="ring" cx="44" cy="44" r="41"/>
    <g class="glyph">
      <circle cx="44" cy="30" r="6"/>
      <path d="M34 46c0-6 4-9 10-9s10 3 10 9"/>
      <path d="M30 50l2 4 4 .5-3 3 1 4-4-2-4 2 1-4-3-3 4-.5zM44 50l2 4 4 .5-3 3 1 4-4-2-4 2 1-4-3-3 4-.5zM58 50l2 4 4 .5-3 3 1 4-4-2-4 2 1-4-3-3 4-.5z"/>
    </g>
  </svg>

  <section class="value value--left" style="top:753px">
    <h2 class="value__name">CLIENT FOCUSED</h2>
    <p class="value__text">We provide a personal service<br>that goes above the standards<br>of professional care.</p>
  </section>
  <section class="value value--right" style="top:753px">
    <h2 class="value__name">RELENTLESS</h2>
    <p class="value__text">We believe that the longer we try<br>to do our best, the better<br>we become.</p>
  </section>

  <section class="promise">
    <h2 class="promise__name">BRAND PROMISE</h2>
    <p class="promise__text">Trust, Transparency and Dependability</p>
  </section>

  <section class="services">
    <div class="service service--left">
      <h3 class="service__name">TAX</h3>
      <p class="service__text">Maple Finch provides all clients<br>with a trusted tax advisor who<br>provides accuracy in all filings<br>and ensures your compliance<br>with all government agencies.</p>
    </div>
    <div class="service service--right">
      <h3 class="service__name">ACCOUNTING</h3>
      <p class="service__text">Maple Finch provides all<br>business owners with the<br>financial visibility needed to<br>foster growth and<br>facilitate goals.</p>
    </div>
  </section>

  <p class="site"><span class="site__name">maplefinchadvisory</span>.com</p>
</main>
</body>
</html>
```